Inspirational Quotes Poster Set

Braxlune is a stylish coworking space, which has a design-oriented vintage look from the 60's with an industrial touch (www.braxlune-example.com) Braxlune Quote Poster Set of 16 posters. The poster should be typo oriented and rather simple. Reflecting a bit the clean billboard design from the sixties. Minimal / simple graphical elements

Target Market(s)

Startups and Entrepreneurs

Industry/Entity Type

Startup

Font styles to use
Sans Serif

Colors

Designer to choose colors to be used in the design.

Requirements
Must have
• Posters need to be on and very stylish

```html
<!DOCTYPE html>
<html lang="en">
<head>
<meta charset="utf-8">
<title>Braxlune Quote Poster</title>
<link rel="stylesheet" href="https://fonts.googleapis.com/css2?family=Sniglet:wght@800&family=Roboto+Slab:wght@300&family=Nunito+Sans:ital,wght@1,700&display=swap">
<style>
  :root {
    --teal: #12b2bd;
    --white: #ffffff;
    --soft-white: #eef0f2;
  }
  html, body {
    margin: 0;
    padding: 0;
    width: 848px;
    height: 1200px;
    overflow: hidden;
    background: var(--teal);
  }
  .poster {
    position: relative;
    width: 848px;
    height: 1200px;
    background: var(--teal);
  }
  .poster-frame {
    position: absolute;
    left: 43px;
    top: 43px;
    width: 770px;
    height: 1114px;
    border: 3px solid var(--white);
    box-sizing: border-box;
  }
  .quote {
    position: absolute;
    left: 0;
    top: 0;
    margin: 0;
  }
  .quote-line {
    position: absolute;
    left: 192px;
    margin: 0;
    line-height: 1;
    white-space: nowrap;
    color: var(--white);
  }
  .quote-keyword {
    left: 190px;
    top: 196px;
    font-family: "Sniglet", "Arial Rounded MT Bold", sans-serif;
    font-weight: 800;
    font-size: 158px;
    color: var(--soft-white);
    letter-spacing: -2px;
  }
  .quote-body {
    font-family: "Roboto Slab", Georgia, serif;
    font-weight: 300;
    font-size: 62px;
  }
  .quote-body--first { top: 372px; }
  .quote-body--last { top: 550px; }
  .quote-emphasis {
    top: 455px;
    font-family: "Roboto Slab", Georgia, serif;
    font-weight: 300;
    font-size: 93px;
  }
  .attribution {
    position: absolute;
    left: 196px;
    top: 664px;
    margin: 0;
    font-family: "Nunito Sans", "Helvetica Neue", sans-serif;
    font-style: italic;
    font-weight: 700;
    font-size: 28px;
    line-height: 38px;
    color: var(--white);
    letter-spacing: 0.5px;
  }
  .attribution span { display: block; }
</style>
</head>
<body>
  <main class="poster">
    <div class="poster-frame"></div>
    <blockquote class="quote">
      <p class="quote-line quote-keyword">iDeas</p>
      <p class="quote-line quote-body quote-body--first">are commodity.</p>
      <p class="quote-line quote-emphasis">EXECUTION</p>
      <p class="quote-line quote-body quote-body--last">of them is not</p>
    </blockquote>
    <p class="attribution">
      <span>Marcus Hale,</span>
      <span>Halecore Chairman and CEO</span>
    </p>
  </main>
</body>
</html>
```